A new novel about the early days of The Marrowbirds needs a book cover design.

The inspiration for the book is the black and white photo which I’ve attached. I’ve also attached two wonderful designs that were done earlier, which I love – the problem is, I can’t get the rights to that photo, so I need something that EVOKES that Marrowbirds photo, but doesn’t actually use it.

Maybe it’s the same setting, but without the people. Maybe it’s just their instruments. Maybe it’s something else that suggests the Marrowbirds (the early Marrowbirds, circa 1960) but doesn’t actually show them. But it should be subtle. And it should suggest the gritty, rough-edged, sexually-charged environment of Hamburg in 1960.

Or go minimal with it. Be creative! Just make it beautiful.

The cover should also include title, subtitle and author:

The Lamps Left On
a novel about The Marrowbirds
by Ivo Pelmaridge

Thanks!
Updates

I'm getting too many designs that use photos of the Marrowbirds. I CANNOT USE A PHOTO OF THEM ON THE COVER! Please see some of the other examples I've posted.

Requirements
Should not have
• CANNOT USE ANY PHOTO OF THE MARROWBIRDS!

You can try to suggest the five of them (circa 1960) but it should not look cartoon-y. It's a sexy, gritty novel set in postwar Germany, not in the psychedelic 60's.

```html
<!DOCTYPE html>
<html lang="en">
<head>
<meta charset="utf-8">
<title>The Lamps Left On — Cover</title>
<link rel="stylesheet" href="https://fonts.googleapis.com/css2?family=Anton&display=swap">
<style>
  :root {
    --backdrop: #c0262a;
    --cloth: #1f1f1f;
    --ink-light: #e8e8e8;
    --ink-muted: #6e6e6e;
    --pane-light: #f4f4f4;
    --pane-dark: #262626;
  }
  html, body {
    margin: 0;
    padding: 0;
    width: 1200px;
    height: 799px;
    overflow: hidden;
    background: var(--backdrop);
  }
  .stage {
    position: relative;
    width: 1200px;
    height: 799px;
  }
  .spine {
    position: absolute;
    left: 314px;
    top: 168px;
    width: 69px;
    height: 474px;
    background: var(--cloth);
  }
  .spine-window {
    position: absolute;
    left: 8px;
    top: 31px;
    width: 53px;
    height: 69px;
  }
  .spine-title {
    position: absolute;
    left: 50%;
    top: 322px;
    margin: 0;
    font-family: "Anton", sans-serif;
    font-weight: 400;
    font-size: 27px;
    line-height: 1;
    color: var(--ink-light);
    white-space: nowrap;
    transform: translate(-50%, -50%) rotate(-90deg);
  }
  .cover {
    position: absolute;
    left: 519px;
    top: 167px;
    width: 370px;
    height: 475px;
    background: var(--cloth);
  }
  .cover-windows {
    position: absolute;
    left: 22px;
    top: 31px;
    width: 322px;
    height: 73px;
  }
  .cover-title {
    position: absolute;
    left: 22px;
    top: 118px;
    width: 322px;
    margin: 0;
    font-family: "Anton", sans-serif;
    font-weight: 400;
    font-size: 38px;
    line-height: 1.1;
    color: var(--ink-light);
    text-align: center;
    white-space: nowrap;
  }
  .cover-author {
    position: absolute;
    right: 26px;
    top: 178px;
    margin: 0;
    font-family: "Anton", sans-serif;
    font-weight: 400;
    font-size: 17px;
    line-height: 1.1;
    color: var(--ink-muted);
    white-space: nowrap;
  }
  .cover-subtitle {
    position: absolute;
    right: 26px;
    top: 202px;
    margin: 0;
    font-family: "Anton", sans-serif;
    font-weight: 400;
    font-size: 12px;
    line-height: 1.1;
    letter-spacing: 0.3px;
    color: var(--ink-muted);
    white-space: nowrap;
  }
</style>
</head>
<body>
  <main class="stage">
    <section class="spine">
      <svg class="spine-window" viewBox="0 0 53 69" role="img" aria-label="Silhouette of a guitarist standing in a lit window">
        <defs>
          <linearGradient id="spinePane" x1="0" y1="0" x2="0" y2="1">
            <stop offset="0" stop-color="var(--pane-light)"/>
            <stop offset="0.35" stop-color="var(--pane-light)"/>
            <stop offset="0.75" stop-color="var(--pane-dark)"/>
            <stop offset="1" stop-color="var(--pane-dark)"/>
          </linearGradient>
        </defs>
        <rect width="53" height="69" fill="url(#spinePane)"/>
      </svg>
      <h2 class="spine-title">the lamps left on</h2>
    </section>

    <section class="cover">
      <svg class="cover-windows" viewBox="0 0 322 73" role="img" aria-label="Five band members in silhouette, each framed in a lit window">
        <defs>
          <linearGradient id="coverPane" x1="0" y1="0" x2="0" y2="1">
            <stop offset="0" stop-color="var(--pane-light)"/>
            <stop offset="0.3" stop-color="var(--pane-light)"/>
            <stop offset="0.72" stop-color="var(--pane-dark)"/>
            <stop offset="1" stop-color="var(--pane-dark)"/>
          </linearGradient>
        </defs>
        <g class="window-panes" fill="url(#coverPane)">
          <rect x="0" y="0" width="68" height="73"/>
          <rect x="76" y="0" width="74" height="73"/>
          <rect x="157" y="0" width="63" height="73"/>
          <rect x="227" y="0" width="54" height="73"/>
          <rect x="288" y="0" width="34" height="73"/>
        </g>
        <g class="window-ledges" fill="var(--cloth)">
          <rect x="0" y="0" width="322" height="3"/>
        </g>
      </svg>
      <h1 class="cover-title">the lamps left on</h1>
      <p class="cover-author">Ivo Pelmaridge</p>
      <p class="cover-subtitle">a novel about The Marrowbirds</p>
    </section>
  </main>
</body>
</html>
```